Outdoor mass notification company needing business card design.

Our company name is Harborline Signal Systems Inc located in Amory Mississippi and we sell and maintain "Corvath" Mass Notification Sirens in the US. Outdoor sirens notify people of certain severe dangers such as tornados, severe thunderstorms, flooding, hurricanes and tsunamis. We also serve the oil and gas refining industries to warn of Chemical releases, fires, and lightning alerts.

Contact Information for Business Card

Name, title, cell number, email address

Requirements
Nice to have
• The Corvath logo and also the Tallbrook logo.

```html
<!DOCTYPE html>
<html lang="en">
<head>
<meta charset="utf-8">
<title>Harborline Signal Systems – Business Card</title>
<link rel="stylesheet" href="https://fonts.googleapis.com/css2?family=Montserrat:wght@400;500;700&family=Cinzel:wght@600&display=swap">
<style>
  :root {
    --backdrop: #e9eaec;
    --card-white: #ffffff;
    --navy: #1d3f7a;
    --logo-teal: #1f5678;
    --ink: #1c1c1c;
    --back-top: #0d4866;
    --back-bottom: #07344f;
    --logo-light: #8fc0de;
  }
  * { box-sizing: border-box; margin: 0; padding: 0; }
  html, body { width: 1200px; height: 1200px; overflow: hidden; }
  body {
    background: var(--backdrop);
    font-family: "Montserrat", Arial, sans-serif;
    display: flex;
    flex-direction: column;
    align-items: center;
    justify-content: center;
    gap: 60px;
  }
  .card {
    width: 840px;
    height: 480px;
    border-radius: 34px;
    position: relative;
    overflow: hidden;
    box-shadow: 0 6px 18px rgba(0,0,0,0.12);
  }
  .card--front { background: var(--card-white); }
  .card--back {
    background: linear-gradient(160deg, var(--back-top), var(--back-bottom));
    display: flex;
    align-items: center;
    justify-content: center;
  }
  .brand {
    font-family: "Cinzel", Georgia, serif;
    font-weight: 600;
    text-transform: uppercase;
    line-height: 1.05;
    display: flex;
    align-items: center;
    gap: 18px;
  }
  .brand__mark { border-radius: 50%; flex: none; }
  .brand--front {
    position: absolute;
    top: 110px;
    right: 70px;
    color: var(--logo-teal);
    font-size: 30px;
  }
  .brand--front .brand__mark { width: 22px; height: 22px; background: var(--logo-teal); }
  .brand--back { color: var(--logo-light); font-size: 56px; }
  .brand--back .brand__mark { width: 40px; height: 40px; background: var(--logo-light); }

  .contact {
    position: absolute;
    left: 70px;
    bottom: 60px;
    color: var(--ink);
  }
  .contact__name {
    color: var(--navy);
    font-weight: 700;
    font-size: 38px;
    letter-spacing: 0.5px;
    line-height: 1;
  }
  .contact__title {
    font-size: 20px;
    letter-spacing: 1px;
    margin: 6px 0 14px;
  }
  .contact__list { list-style: none; font-size: 19px; line-height: 1.35; }
  .contact__list li { display: flex; align-items: flex-start; gap: 12px; }
  .contact__icon { width: 20px; height: 20px; flex: none; margin-top: 3px; fill: var(--navy); }
</style>
</head>
<body>
  <section class="card card--front">
    <div class="brand brand--front">
      <span class="brand__mark"></span>
      <span>Harborline<br>Signal Systems</span>
    </div>
    <div class="contact">
      <h1 class="contact__name">FULL NAME</h1>
      <p class="contact__title">POSITION</p>
      <ul class="contact__list">
        <li><svg class="contact__icon" viewBox="0 0 24 24"><path d="M6.6 10.8a15 15 0 0 0 6.6 6.6l2.2-2.2c.3-.3.7-.4 1-.2 1.1.4 2.3.6 3.6.6.6 0 1 .4 1 1V20c0 .6-.4 1-1 1A17 17 0 0 1 3 4c0-.6.4-1 1-1h3.5c.6 0 1 .4 1 1 0 1.3.2 2.5.6 3.6.1.3 0 .7-.2 1z"/></svg>(000) 000 0000</li>
        <li><svg class="contact__icon" viewBox="0 0 24 24"><path d="M2 5h20v14H2z M2 5l10 8 10-8" fill="none" stroke="#1d3f7a" stroke-width="2"/></svg>email@company.com</li>
        <li><svg class="contact__icon" viewBox="0 0 24 24"><g fill="none" stroke="#1d3f7a" stroke-width="1.8"><circle cx="12" cy="12" r="9.5"/><ellipse cx="12" cy="12" rx="4" ry="9.5"/><path d="M2.5 12h19M4 7h16M4 17h16"/></g></svg>www.company.com</li>
        <li><svg class="contact__icon" viewBox="0 0 24 24"><path d="M12 2a7 7 0 0 0-7 7c0 5 7 13 7 13s7-8 7-13a7 7 0 0 0-7-7zm0 9.5A2.5 2.5 0 1 1 12 6.5a2.5 2.5 0 0 1 0 5z"/></svg><span>123 Name Street, 000<br>Your City, 00000-000</span></li>
      </ul>
    </div>
  </section>

  <section class="card card--back">
    <div class="brand brand--back">
      <span class="brand__mark"></span>
      <span>Harborline<br>Signal Systems</span>
    </div>
  </section>
</body>
</html>
```